Accounting services

Looking for a Business card & Logo design

company name - QUELM ACCOUNTING & TAXATION SOLUTIONS

name - Corwin Belto

position - Accountant / Business Consultant

email - "undecided"

Tel : (868) 512-0000 / (868) 287-0000

**PUT THESE TO THE BACK**
Accounting - VAT * INCOME/CORP TAX * RETURNS

REGISTRATION - VAT * NIS * Company Registration/Business Plan

```html
<!DOCTYPE html>
<html lang="en">
<head>
<meta charset="utf-8">
<title>Quelm Accounting &amp; Taxation Solutions – Business Card</title>
<link rel="stylesheet" href="https://fonts.googleapis.com/css2?family=Cinzel:wght@400;500&family=Tinos:wght@400&display=swap">
<style>
  :root {
    --backdrop: #d9d4cc;
    --card-black: #0b0b0b;
    --card-black-sheen: #2a2a2a;
    --card-white: #f7f7f7;
    --card-white-shade: #e6e6e6;
    --ink-light: #f2f2f2;
    --ink-light-soft: #cfcfcf;
    --ink-dark: #1c1c1c;
    --ink-dark-soft: #555555;
    --rule: #3a3a3a;
  }
  * { box-sizing: border-box; margin: 0; padding: 0; }
  html, body { width: 1200px; height: 902px; overflow: hidden; }
  body {
    background: var(--backdrop);
    position: relative;
    font-family: "Tinos", "Times New Roman", serif;
  }
  .card {
    position: absolute;
    width: 600px;
    height: 343px;
    box-shadow: 0 14px 30px rgba(0,0,0,0.35);
  }
  /* Back of card */
  .card--back {
    left: 70px;
    top: 80px;
    background: linear-gradient(125deg, var(--card-black) 0%, var(--card-black-sheen) 38%, var(--card-black) 62%);
    color: var(--ink-light);
  }
  .card--back .company {
    position: absolute;
    right: 60px;
    top: 95px;
    text-align: right;
  }
  .company__name {
    font-family: "Cinzel", "Times New Roman", serif;
    font-weight: 500;
    font-size: 27px;
    letter-spacing: 0.5px;
    line-height: 1.1;
  }
  .company__tag {
    font-family: "Cinzel", "Times New Roman", serif;
    font-weight: 400;
    font-size: 24px;
    letter-spacing: 2px;
    margin-right: 100px;
    line-height: 1.15;
  }
  .card--back .company__tag { color: var(--ink-light-soft); }
  .services {
    position: absolute;
    right: 40px;
    bottom: 62px;
    text-align: right;
    font-size: 14px;
    line-height: 1.45;
    color: var(--ink-light);
  }
  /* Front of card */
  .card--front {
    left: 530px;
    top: 490px;
    background: radial-gradient(ellipse at 40% 30%, #ffffff 0%, var(--card-white) 55%, var(--card-white-shade) 100%);
    color: var(--ink-dark);
  }
  .card--front .company {
    position: absolute;
    right: 58px;
    top: 60px;
    text-align: right;
  }
  .card--front .company__tag { color: var(--ink-dark-soft); }
  .person {
    position: absolute;
    right: 275px;
    top: 225px;
    text-align: right;
  }
  .person__name {
    font-family: "Cinzel", "Times New Roman", serif;
    font-size: 24px;
    letter-spacing: 0.5px;
    line-height: 1.1;
  }
  .person__role {
    font-size: 13px;
    color: var(--ink-dark-soft);
  }
  .divider {
    position: absolute;
    left: 345px;
    top: 180px;
    width: 1px;
    height: 110px;
    background: var(--rule);
  }
  .contact {
    position: absolute;
    left: 362px;
    top: 182px;
    list-style: none;
    font-size: 13px;
    line-height: 1.5;
    color: var(--ink-dark);
  }
  .contact li { display: flex; align-items: center; gap: 6px; }
  .contact svg { width: 11px; height: 11px; fill: var(--ink-dark); flex: none; }
</style>
</head>
<body>

<section class="card card--back" aria-label="Card back">
  <div class="company">
    <p class="company__name">QUELM ACCOUNTING &amp; TAXATION</p>
    <p class="company__tag">SOLUTIONS</p>
  </div>
  <div class="services">
    <p>Accounting - VAT * INCOME/CORP TAX * RETURNS</p>
    <p>REGISTRATION - VAT * NIS * Company Registration/Business Plan</p>
  </div>
</section>

<section class="card card--front" aria-label="Card front">
  <div class="company">
    <p class="company__name">QUELM ACCOUNTING &amp; TAXATION</p>
    <p class="company__tag">SOLUTIONS</p>
  </div>
  <div class="person">
    <p class="person__name">CORWIN BELTO</p>
    <p class="person__role">Accountant / Business Consultant</p>
  </div>
  <div class="divider"></div>
  <ul class="contact">
    <li>
      <svg viewBox="0 0 12 12" aria-hidden="true"><path d="M1 4c0-2 2-3 5-3s5 1 5 3l-2 .6-.6-1.4H3.6L3 4.6zM3 5h6l1.5 5.5h-9z"/><circle cx="6" cy="7.5" r="1.3" fill="#fff"/></svg>
      <span>(868) 512-0000</span>
    </li>
    <li>
      <svg viewBox="0 0 12 12" aria-hidden="true"><path d="M1 4c0-2 2-3 5-3s5 1 5 3l-2 .6-.6-1.4H3.6L3 4.6zM3 5h6l1.5 5.5h-9z"/><circle cx="6" cy="7.5" r="1.3" fill="#fff"/></svg>
      <span>(868) 287-0000</span>
    </li>
    <li>
      <svg viewBox="0 0 12 12" aria-hidden="true"><path d="M1 2.5h10v7H1z"/><path d="M1 2.5l5 4 5-4" fill="none" stroke="#fff" stroke-width="1"/></svg>
      <span>corwin@quelmtaxsolutions.com</span>
    </li>
  </ul>
</section>

</body>
</html>
```